Frozen Yoghurt
Aufgabenstellung
Es soll eine Postkarte erstellt werden
auf die Vorteile des Produkts dargestellt werden
- kein fett (98% fettfrei)
- keine künstlichen süssungsmittel
- low calorien
- Viel Calcium
- Viel Eiweiss
- Vitamine durch Frucht topping
Die Postkarte soll gleichzeitig dazu dienen dass man sie mit zu uns ins Geschäft bringt und dann ein gratis Muster bekommt.
Mitbewerber: www.iwantaquirl.com, www.bluemaple.com

```html
<!DOCTYPE html>
<html lang="de">
<head>
<meta charset="utf-8">
<title>Frozen Yoghurt Postkarte</title>
<link rel="stylesheet" href="https://fonts.googleapis.com/css2?family=Kaushan+Script&family=Montserrat:wght@400;700&display=swap">
<style>
  :root {
    --raspberry: #e0204f;
    --lime: #6cbd2a;
    --ink: #111111;
    --white: #ffffff;
    --cream: #f3efe6;
    --rule: #9a9a9a;
    --mint: #cfe8c4;
  }
  * { margin: 0; padding: 0; box-sizing: border-box; }
  html, body { width: 800px; height: 1200px; overflow: hidden; background: var(--white); }
  .canvas { position: relative; width: 800px; height: 1200px; font-family: "Montserrat", sans-serif; }

  .card-front { position: absolute; left: 0; top: 0; width: 800px; height: 570px; overflow: hidden; }
  .front-photo {
    position: absolute; inset: 0;
    background:
      radial-gradient(circle at 28% 18%, rgba(214,40,70,.75) 0 70px, transparent 90px),
      radial-gradient(circle at 72% 12%, rgba(60,70,100,.8) 0 60px, transparent 80px),
      radial-gradient(circle at 4% 10%, rgba(50,55,85,.8) 0 60px, transparent 80px),
      radial-gradient(circle at 40% 30%, rgba(210,170,100,.5) 0 40px, transparent 70px),
      linear-gradient(180deg, #f1ece2 0%, #f7f4ee 60%, #ffffff 100%);
  }

  .card-back { position: absolute; left: 0; top: 624px; width: 800px; height: 576px; overflow: hidden; }
  .back-backdrop { position: absolute; inset: 0; }

  .slogan {
    position: absolute; right: 32px;
    font-family: "Kaushan Script", cursive; font-size: 36px; color: var(--white);
    text-shadow: 2px 2px 3px rgba(0,0,0,.55);
    letter-spacing: 1px;
  }
  .brand-bar {
    position: absolute; left: 276px; width: 524px; height: 132px;
    background: var(--raspberry);
  }
  .brand-mark {
    position: absolute; left: 0; top: 0; width: 130px; height: 132px; background: var(--ink);
    display: flex; flex-direction: column; align-items: center; justify-content: center; gap: 10px;
  }
  .brand-mark .dot { width: 46px; height: 46px; border-radius: 50%; background: var(--lime); }
  .brand-mark .name { color: var(--lime); font-size: 15px; font-weight: 700; }
  .product-title {
    position: absolute; left: 170px; top: 20px; color: var(--white);
    font-size: 50px; font-weight: 400; letter-spacing: 1px; line-height: 1;
  }
  .product-sub {
    position: absolute; left: 232px; top: 56px; color: var(--lime);
    font-family: "Kaushan Script", cursive; font-size: 50px; line-height: 1;
  }

  .benefits {
    position: absolute; right: 370px; top: 62px; list-style: none; text-align: right;
    font-family: "Kaushan Script", cursive; font-size: 18px; line-height: 26px; color: var(--raspberry);
  }
  .address-lines { position: absolute; left: 498px; top: 170px; width: 302px; }
  .address-lines span { display: block; height: 1px; background: var(--rule); margin-bottom: 42px; }
  .address-lines span:nth-child(2) { margin-left: 10px; }
  .address-lines span:nth-child(3) { margin-left: 28px; }
  .address-lines span:nth-child(4) { margin-left: 56px; }

  .product-photo {
    position: absolute; left: 0; top: 190px; width: 430px; height: 356px;
    background:
      radial-gradient(ellipse at 30% 70%, rgba(190,30,50,.6) 0 60px, transparent 110px),
      radial-gradient(ellipse at 62% 42%, rgba(40,45,70,.75) 0 60px, transparent 90px),
      radial-gradient(ellipse at 28% 38%, rgba(250,248,240,.95) 0 70px, transparent 110px),
      radial-gradient(ellipse at 58% 18%, rgba(252,252,250,.95) 0 50px, transparent 80px);
  }
  .voucher {
    position: absolute; right: 18px; bottom: 14px; font-size: 12px; font-weight: 700; color: var(--ink);
  }
</style>
</head>
<body>
<main class="canvas">
  <section class="card-front">
    <div class="front-photo" role="img" aria-label="Frozen Yoghurt mit Himbeeren, Heidelbeeren, Brombeeren und Granola in Nahaufnahme"></div>
    <p class="slogan" style="top:362px;">.. so lecker und so leicht</p>
    <div class="brand-bar" style="top:420px;">
      <div class="brand-mark"><span class="dot"></span><span class="name">Kühlwerk</span></div>
      <h1 class="product-title">FROZEN</h1>
      <p class="product-sub">Yoghurt</p>
    </div>
  </section>

  <section class="card-back">
    <svg class="back-backdrop" width="800" height="576" viewBox="0 0 800 576" role="img" aria-label="Verblasstes Foto von Frozen Yoghurt mit Beeren">
      <defs>
        <linearGradient id="fade" x1="0" y1="0" x2="1" y2="0">
          <stop offset="0" stop-color="#e4e0d8"/>
          <stop offset="1" stop-color="#f4f1ec"/>
        </linearGradient>
        <radialGradient id="berry" cx="0.5" cy="0.5" r="0.5">
          <stop offset="0" stop-color="#e8a9b5"/>
          <stop offset="1" stop-color="#e8a9b5" stop-opacity="0"/>
        </radialGradient>
        <linearGradient id="mint" x1="0" y1="0" x2="0" y2="1">
          <stop offset="0" stop-color="#cfe8c4" stop-opacity="0"/>
          <stop offset="0.5" stop-color="#c6e3b8"/>
          <stop offset="1" stop-color="#d9eccf"/>
        </linearGradient>
      </defs>
      <rect width="800" height="576" fill="url(#fade)"/>
      <circle cx="220" cy="110" r="110" fill="url(#berry)"/>
      <path d="M0 120 C60 200 70 420 0 560 Z" fill="url(#mint)"/>
      <rect y="536" width="800" height="40" fill="#dcecd3"/>
      <ellipse cx="720" cy="210" rx="330" ry="340" fill="#ffffff"/>
    </svg>

    <ul class="benefits">
      <li>mit nur 2% Fett</li>
      <li>ohne künstliche Süssungsmittel</li>
      <li>wenig Kalorien</li>
      <li>mit viel Calcium &amp; Eiweiß</li>
      <li>Vitamine durch das Frucht topping</li>
    </ul>

    <div class="address-lines"><span></span><span></span><span></span><span></span></div>

    <div class="product-photo" role="img" aria-label="Becher Frozen Yoghurt mit Himbeersoße und Granola sowie Softeis mit Brombeeren"></div>

    <p class="slogan" style="top:346px;">.. so lecker und so leicht</p>
    <div class="brand-bar" style="top:396px;">
      <div class="brand-mark"><span class="dot"></span><span class="name">Kühlwerk</span></div>
      <h2 class="product-title">FROZEN</h2>
      <p class="product-sub">Yoghurt</p>
    </div>

    <p class="voucher">Mit diesem Flyer erhalten Sie einen Frozen Yoghurt GRATIS</p>
  </section>
</main>
</body>
</html>
```